Bref créative
Valmirock Stationary Design
Business Cards, Letterhead, etc....
Professional
Dorian K. Pelletrow
Chief Executive Officer
2718 N. Birch Ln.
Suite K-42
Tempe, AZ 85107-3318
XXX-XXX-XXXX
dorian@valmirock-example.com
http://www.valmirock-example.com/
See our website for our business areas and marketing information.
Back of the business card should be branded, but simple. Maybe our company monogram. There should be enough space to write notes on the back of the card.
Contains several versions of our logo for stationary design.

```html
<!DOCTYPE html>
<html lang="en">
<head>
<meta charset="utf-8">
<title>Valmirock Laboratories – Business Card</title>
<link rel="stylesheet" href="https://fonts.googleapis.com/css2?family=Open+Sans:wght@400;600;700&display=swap">
<style>
  :root {
    --teal-deep: #0b3444;
    --teal-mid: #0f5d70;
    --teal-bright: #1b93a8;
    --cyan-accent: #3cc6ea;
    --white: #ffffff;
    --ink: #27333b;
    --link-teal: #1a9ab5;
  }
  * { margin: 0; padding: 0; box-sizing: border-box; }
  html, body {
    width: 1200px;
    height: 686px;
    overflow: hidden;
    background: #e9eef0;
  }
  .card {
    position: relative;
    width: 1200px;
    height: 686px;
    overflow: hidden;
    font-family: "Open Sans", Arial, sans-serif;
    color: var(--white);
    background: linear-gradient(100deg, var(--teal-deep) 0%, var(--teal-mid) 45%, var(--teal-bright) 100%);
  }
  .brand-field {
    position: absolute;
    left: 720px;
    top: -60px;
    width: 560px;
    height: 820px;
    border-radius: 48% 0 0 46%;
    background: radial-gradient(ellipse at 62% 48%, #ffffff 0%, #ffffff 42%, rgba(210, 236, 242, 0.85) 62%, rgba(27, 147, 168, 0) 82%);
  }
  .brand {
    position: absolute;
    left: 52px;
    top: 98px;
    display: flex;
    align-items: center;
    gap: 22px;
  }
  .brand-dot {
    width: 78px;
    height: 78px;
    border-radius: 50%;
    background: var(--cyan-accent);
  }
  .brand-name {
    font-weight: 700;
    font-size: 58px;
    letter-spacing: 3px;
    color: var(--white);
    text-transform: uppercase;
  }
  .identity {
    position: absolute;
    right: 735px;
    top: 306px;
    text-align: right;
  }
  .person-name {
    font-weight: 600;
    font-size: 36px;
    color: var(--cyan-accent);
    line-height: 1.2;
  }
  .person-title {
    font-size: 25px;
    line-height: 1.4;
  }
  .address {
    position: absolute;
    right: 735px;
    top: 432px;
    text-align: right;
    font-size: 23px;
    line-height: 32px;
  }
  .contact {
    position: absolute;
    font-size: 23px;
    white-space: nowrap;
  }
  .contact-label { color: var(--cyan-accent); }
  .contact-phone { left: 192px; top: 510px; }
  .contact-cell  { left: 247px; top: 547px; }
  .contact-fax   { left: 276px; top: 584px; }
  .contact-email { left: 154px; top: 624px; }
  .website {
    position: absolute;
    right: 38px;
    top: 318px;
    font-size: 29px;
    color: var(--ink);
  }
  .website-domain { color: var(--link-teal); }
</style>
</head>
<body>
  <main class="card">
    <div class="brand-field" role="img" aria-label="Large white brand decoration area"></div>

    <div class="brand">
      <span class="brand-dot"></span>
      <span class="brand-name">Valmirock</span>
    </div>

    <section class="identity">
      <p class="person-name">Dorian K. Pelletrow</p>
      <p class="person-title">Chief Executive Officer</p>
    </section>

    <address class="address" style="font-style: normal;">
      <p>2718 N. Birch Ln. Suite K-42</p>
      <p>Tempe, AZ 85107-3318</p>
    </address>

    <p class="contact contact-phone"><span class="contact-label">Phone:</span> 480-555-0143</p>
    <p class="contact contact-cell"><span class="contact-label">Cell:</span> XXX-XXX-XXXX</p>
    <p class="contact contact-fax"><span class="contact-label">Fax:</span> 480-555-0144</p>
    <p class="contact contact-email"><span class="contact-label">Email:</span> dorian@valmirock-example.com</p>

    <p class="website">www.<span class="website-domain">valmirock-example</span>.com</p>
  </main>
</body>
</html>
```